Creative label for amber glass candle jar.

We are a candle company. Our products are handmade by us and natural. We are looking for something minimalistic and unique. We need a label for our candle jars (amber glass with black lid). Our current label doesn't match these requirements. We would like our products to be stocked in London shop, therefore design has to be up to a high standard. Jar specification Diameter (mm) 65 Height without cap (mm) 80. We want the new design to be different from the current one. It's just a guide for wording.
We should be able adjust the label, to change scent name.
Our scents are
*Coconut & Vanilla
*Lavender
*Bergamot
*Italian Garden
*Hygge
*Eucalyptus & Peppermint
*Coffee
*Cedarwood & Juniperberry
To know more about us, visit our website www.fenwickbrae.com or instagram.com/fenwickbrae
Good luck!
Industry/Entity Type
It Company
Colors
Designer to choose colors to be used in the design.
Requirements
Must have
- * I have attached two of our logos, label design must include one of them.
- *has to mention that it's made in London
- *has to say that candle is natural/made with essential oils
- *has to have scent name and No. on it..
- Label can be vertical or horizontal, but has to be square/rectangular,.
Should not have
- Label should not be round

```html
<!DOCTYPE html>
<html lang="en">
<head>
<meta charset="utf-8">
<title>Fenwick Brae – No. 06 Candle Label</title>
<link rel="stylesheet" href="https://fonts.googleapis.com/css2?family=Josefin+Sans:wght@300;400&family=Pinyon+Script&display=swap">
<style>
  :root {
    --backdrop: #ece8e2;
    --label-paper: #ffffff;
    --ink: #4a4a4a;
    --ink-strong: #3f3f3f;
    --panel-text: #ffffff;
  }
  * { margin: 0; padding: 0; box-sizing: border-box; }
  html, body { width: 1200px; height: 1000px; overflow: hidden; }
  body {
    background: var(--backdrop);
    font-family: "Josefin Sans", sans-serif;
    color: var(--ink);
    position: relative;
  }
  .label {
    position: absolute;
    left: 75px; top: 260px;
    width: 1050px; height: 479px;
    background: var(--label-paper);
    box-shadow: 0 4px 18px rgba(0,0,0,0.08);
  }
  .label-frame {
    position: absolute;
    left: 24px; top: 71px;
    width: 1000px; height: 388px;
    border: 3px solid var(--ink);
    border-radius: 17px;
  }
  .brand-name {
    position: absolute;
    left: 50%; top: 78px;
    transform: translate(-50%, -50%);
    background: var(--label-paper);
    padding: 0 30px;
    font-weight: 400;
    font-size: 64px;
    letter-spacing: 4px;
    text-transform: lowercase;
    color: var(--ink-strong);
    white-space: nowrap;
    line-height: 1;
  }
  .scent-number {
    position: absolute;
    left: 53px; top: 92px;
    display: flex; align-items: baseline;
    line-height: 1;
  }
  .scent-number .number-mark {
    font-family: "Pinyon Script", cursive;
    font-size: 60px;
    margin-right: 8px;
  }
  .scent-number .number-value {
    font-weight: 300;
    font-size: 76px;
  }
  .scent-name {
    position: absolute;
    left: 118px; top: 224px;
    width: 765px;
    overflow: hidden;
    font-weight: 300;
    font-size: 52px;
    letter-spacing: 0.5px;
    text-transform: uppercase;
    line-height: 1;
    white-space: nowrap;
  }
  .scent-rule {
    position: absolute;
    left: 87px; top: 300px;
    width: 800px; height: 3px;
    background: var(--ink);
  }
  .product-panel {
    position: absolute;
    left: 175px; top: 328px;
    width: 699px; height: 99px;
    background: var(--ink);
    border-radius: 7px;
    display: flex; flex-direction: column;
    align-items: center; justify-content: center;
    color: var(--panel-text);
    font-size: 28px;
    font-variant: small-caps;
    line-height: 1.05;
    letter-spacing: 0.5px;
  }
  .divider-ornament {
    position: absolute;
    left: 902px; top: 104px;
    width: 8px; height: 335px;
    background: linear-gradient(to bottom, transparent, var(--ink) 15%, var(--ink) 85%, transparent);
    border-radius: 4px;
  }
  .origin {
    position: absolute;
    left: 971px; top: 265px;
    transform: translate(-50%, -50%) rotate(-90deg);
    font-size: 34px;
    font-variant: small-caps;
    letter-spacing: 1px;
    white-space: nowrap;
    line-height: 1;
  }
</style>
</head>
<body>
  <section class="label">
    <div class="label-frame"></div>
    <div class="brand-name">fenwick brae</div>
    <div class="scent-number"><span class="number-mark">No.</span><span class="number-value">06</span></div>
    <h1 class="scent-name">Eucalyptus &amp; Peppermint</h1>
    <div class="scent-rule"></div>
    <div class="product-panel">
      <span>Handmade Candle</span>
      <span>with Essenstial Oil</span>
    </div>
    <div class="divider-ornament" role="img" aria-label="Vertical twisted flourish divider"></div>
    <div class="origin">Made in London</div>
  </section>
</body>
</html>
```